Brightmoor Partners Branding Revamp

We are a consulting company, looking for a way to display and promote our brand. We have 2 sides to the business- Brightmoor (financial) and Partners (cyber security). The financial side products relate to business necessities: card processing, website design/hosting/maintenance, VoIP phone systems. The cyber security side promotes a bundled package of 4 solutions: network vulnerability scan, dark web scan, anti-ransomeware/malware software, and image-level backups. We want people to understand that partnering with Brightmoor Partners gives them “Steady Calm, Every Day” (tagline). Current badge and logos uploaded.

Target Market(s)

Small businesses

Contact Information for Business Card

Lena Marwick, Vice President, lena@brightmoorpartners.example, 555-806-1937, www.brightmoorpartners.example

Requirements
Nice to have
• I do prefer the darker background for front and back

```html
<!DOCTYPE html>
<html lang="en">
<head>
<meta charset="utf-8">
<title>Brightmoor Partners — Business Cards</title>
<link rel="stylesheet" href="https://fonts.googleapis.com/css2?family=Michroma&family=Montserrat:wght@300;400&display=swap">
<style>
  :root {
    --paper: #e4e4e4;
    --card-black: #0b0a0b;
    --brand-red: #b3151b;
    --deep-red: #7e1015;
    --bright-red: #d81e25;
    --ink-white: #f4f4f4;
    --display: "Michroma", sans-serif;
    --body: "Montserrat", sans-serif;
  }
  * { box-sizing: border-box; margin: 0; padding: 0; }
  html, body { width: 1200px; height: 800px; overflow: hidden; }
  body { background: var(--paper); position: relative; }

  .card {
    position: absolute;
    top: 228px;
    width: 540px;
    height: 343px;
    background: var(--card-black);
    overflow: hidden;
    color: var(--ink-white);
    box-shadow: 0 10px 24px rgba(0,0,0,0.18);
  }
  .card--services { left: 40px; }
  .card--contact { left: 620px; }
  .card__bands { position: absolute; inset: 0; width: 100%; height: 100%; }

  .services-list {
    position: absolute;
    top: 20px; left: 0; right: 0;
    text-align: center;
    font-family: var(--display);
    font-size: 10px;
    line-height: 20px;
    letter-spacing: 1.2px;
    text-transform: uppercase;
  }

  .brand-name {
    position: absolute;
    left: 0; right: 0;
    text-align: center;
    font-family: var(--display);
    font-weight: 400;
    color: var(--ink-white);
    text-transform: uppercase;
    line-height: 1.35;
  }
  .card--services .brand-name { top: 140px; font-size: 19px; letter-spacing: 6px; }
  .brand-name span { display: block; }

  .tagline {
    position: absolute;
    top: 272px; left: 0; right: 0;
    text-align: center;
    font-family: var(--display);
    font-size: 17px;
    letter-spacing: 7px;
    text-transform: uppercase;
  }

  .card--contact .brand-name {
    top: 128px; left: 40px; right: auto;
    width: 250px;
    font-size: 17px;
    letter-spacing: 5px;
  }

  .contact {
    position: absolute;
    left: 318px; top: 170px;
    font-family: var(--body);
    font-weight: 300;
    font-size: 11.5px;
    line-height: 17px;
  }
  .contact__name {
    font-family: var(--display);
    font-weight: 400;
    color: var(--bright-red);
    font-size: 11px;
    letter-spacing: 2.5px;
    text-transform: uppercase;
    margin-bottom: 6px;
  }
  .contact__address { margin-bottom: 10px; }
</style>
</head>
<body>

  <section class="card card--services" aria-label="Card front: services">
    <svg class="card__bands" viewBox="0 0 778 494" preserveAspectRatio="none" aria-hidden="true">
      <polygon points="0,0 20,0 185,330 185,494 0,494" fill="var(--brand-red)"/>
      <polygon points="0,70 150,330 160,494 0,494" fill="var(--deep-red)" opacity="0.55"/>
      <polygon points="778,0 760,0 530,470 778,494" fill="var(--brand-red)"/>
      <polygon points="778,90 570,470 778,494" fill="var(--deep-red)" opacity="0.55"/>
    </svg>
    <p class="services-list">
      Network vulnerability scan | Dark web scan<br>
      Anti-ransomeware/malware software<br>
      Image-level backups.
    </p>
    <h1 class="brand-name"><span>Brightmoor</span><span>Partners</span></h1>
    <p class="tagline">Steady Calm, Every Day</p>
  </section>

  <section class="card card--contact" aria-label="Card back: contact">
    <svg class="card__bands" viewBox="0 0 778 494" preserveAspectRatio="none" aria-hidden="true">
      <polyline points="170,-10 220,480 560,-10" fill="none" stroke="var(--brand-red)" stroke-width="26" stroke-linejoin="miter"/>
    </svg>
    <h2 class="brand-name"><span>Brightmoor</span><span>Partners</span></h2>
    <div class="contact">
      <p class="contact__name">Lena Marwick</p>
      <p class="contact__address">Suite 4, 18 Larkfield Road<br>Avondale, NY 01200</p>
      <p>555-806-1937<br>lena@brightmoorpartners.example<br>www.brightmoorpartners.example</p>
    </div>
  </section>

</body>
</html>
```